Thistlewood Joinery Website

My client Thistlewood Joinery is looking for a redesign for a Word Press Website. Their current site is at www.thistlewoodjoinery.example They are a custom cabinet company, but also create bathroom, living room, bar and entertainment and bedroom cabinets too. They would like a design that emulates the master craftsman work they do yet a contemporary style.

Their current site was designed using Flash elements.

Target Market(s)

Home owners and builders of high end homes

Industry/Entity Type

Entertainment

Font styles to use
Serif
Decorative

Requirements
Must have
• Must show their work and logo using a contemporary style.
Nice to have
• Sliders that showcase their projects.

```html
<!DOCTYPE html>
<html lang="en">
<head>
<meta charset="utf-8">
<title>Thistlewood Joinery — Custom Kitchen Cabinet Design</title>
<link href="https://fonts.googleapis.com/css2?family=Libre+Baskerville:ital,wght@0,400;0,700;1,400&family=Fira+Sans:wght@300;400;500;600&display=swap" rel="stylesheet">
<style>
:root{
  --wood-dark:#3a2418;
  --wood-mid:#4e3122;
  --wood-light:#5c3b29;
  --nav-bg:#0d1410;
  --green:#3fae49;
  --green-overlay:rgba(46,150,58,.72);
  --pale:#eef2f5;
  --white:#ffffff;
  --ink:#2b2f33;
  --muted:#7b8087;
  --footer-bg:#25272b;
  --footer-line:#34373c;
  --footer-text:#a9adb2;
}
*{box-sizing:border-box;margin:0;padding:0}
html,body{width:1200px;height:2635px;overflow:hidden}
body{position:relative;font-family:"Fira Sans",Arial,sans-serif;color:var(--ink);background:var(--white)}
.abs{position:absolute}
.wood{background:linear-gradient(90deg,var(--wood-dark) 0%,var(--wood-mid) 25%,var(--wood-light) 50%,var(--wood-mid) 75%,var(--wood-dark) 100%)}

/* header */
.site-header{left:0;top:0;width:1200px;height:137px}
.brand{left:175px;top:22px;display:flex;align-items:center;gap:18px}
.brand-mark{width:92px;height:92px;border-radius:50%;background:var(--white)}
.brand-text{display:flex;flex-direction:column;gap:8px}
.brand-name{font-family:"Libre Baskerville",Georgia,serif;font-size:22px;color:var(--white)}
.brand-tagline{font-family:"Libre Baskerville",Georgia,serif;font-style:italic;font-size:13px;line-height:20px;color:#f3ece4}
.social{right:157px;top:30px;display:flex;gap:10px}
.social span{width:25px;height:25px;background:rgba(255,255,255,.28);border-radius:2px}
.call-note{right:157px;top:68px;font-size:12px;color:#cdbfb3;text-align:right}
.call-number{right:157px;top:86px;font-size:28px;font-weight:600;color:var(--white);letter-spacing:.5px}

/* nav */
.main-nav{left:0;top:137px;width:1200px;height:47px;background:var(--nav-bg)}
.main-nav a{position:absolute;top:16px;font-size:12px;color:#cfd6d0;text-decoration:none}
.main-nav a.active{color:var(--white);font-weight:500}
.main-nav a.active::after{content:"";position:absolute;left:0;right:0;top:27px;height:3px;background:var(--green)}

/* hero */
.hero{left:0;top:184px;width:1200px;height:419px;background:linear-gradient(100deg,#8a5a3a 0%,#6b3f26 28%,#b9865a 52%,#7f9a6e 75%,#3f5a3a 100%)}
.hero-card{left:162px;top:258px;width:374px;height:246px;background:rgba(20,20,20,.62);padding:40px 28px}
.hero-eyebrow{font-family:"Libre Baskerville",Georgia,serif;font-size:13px;letter-spacing:1px;color:#5fc266}
.hero-title{font-family:"Libre Baskerville",Georgia,serif;font-style:italic;font-size:33px;color:var(--white);margin:6px 0 18px}
.hero-copy{font-size:16px;line-height:24px;color:#e8e8e8;font-weight:300}
.slide-arrow{width:34px;height:36px;display:flex;align-items:center;justify-content:center;background:rgba(20,20,20,.7)}
.slide-arrow.green{background:var(--green)}

/* categories */
.categories{left:0;top:603px;width:1200px;height:727px;background:var(--pale)}
.tile{position:absolute;width:277px;height:277px;display:flex;flex-direction:column;align-items:center;justify-content:center}
.tile .shade{position:absolute;inset:0;background:rgba(20,20,20,.5)}
.tile.featured .shade{background:var(--green-overlay)}
.tile h3{position:relative;font-family:"Libre Baskerville",Georgia,serif;font-style:italic;font-weight:400;font-size:28px;line-height:36px;color:var(--white);text-align:center;margin-bottom:28px}
.tile .btn{position:relative;width:172px;height:54px;border:2px solid var(--white);color:var(--white);font-size:17px;letter-spacing:1px;display:flex;align-items:center;justify-content:center}
.tile.featured .btn{background:var(--white);color:var(--green);border-color:var(--white)}

/* showcase */
.showcase{left:0;top:1330px;width:1200px;height:471px}
.showcase-eyebrow{left:0;width:1200px;top:64px;text-align:center;font-family:"Libre Baskerville",Georgia,serif;font-size:12px;color:#f0e6dc}
.showcase-title{left:0;width:1200px;top:94px;text-align:center;font-family:"Libre Baskerville",Georgia,serif;font-size:36px;color:var(--white)}
.shot{top:179px;height:223px}
.shot.center{border:4px solid var(--white)}

/* about */
.about-title{left:162px;top:1870px;font-family:"Libre Baskerville",Georgia,serif;font-size:29px;color:var(--ink)}
.about-mark{left:176px;top:1920px;width:110px;height:110px;border-radius:50%;border:3px solid #2c3a2e;background:#f4f6f4}
.about-copy{left:314px;top:1922px;width:280px;font-size:12px;line-height:19px;color:var(--muted)}
.about-copy b{color:var(--ink);font-weight:600}
.learn-more{left:162px;top:2066px;width:126px;height:37px;border:1px solid #d6d9dc;font-size:11px;letter-spacing:1px;color:var(--ink);display:flex;align-items:center;justify-content:center;gap:8px}
.video{left:668px;top:1876px;width:370px;height:218px;border:4px solid #f1f1f1;box-shadow:0 2px 6px rgba(0,0,0,.35);background:linear-gradient(180deg,#5a6470,#8e939a 55%,#4c5058)}
.video-title{left:8px;top:8px;background:rgba(0,0,0,.55);color:#48b2ff;font-size:9px;padding:3px 6px;font-weight:500}
.video-bar{left:8px;right:8px;bottom:8px;height:14px;background:rgba(0,0,0,.6)}
.video-progress{left:26px;top:6px;width:180px;height:2px;background:#48b2ff}

/* footer */
.site-footer{left:0;top:2184px;width:1200px;height:378px;background:var(--footer-bg)}
.foot-col h4{font-family:"Libre Baskerville",Georgia,serif;font-weight:400;font-size:13px;letter-spacing:1px;color:var(--white);margin-bottom:14px}
.foot-col ul{list-style:none;width:200px}
.foot-col li{font-size:10px;color:var(--footer-text);height:30px;line-height:30px;border-bottom:1px solid var(--footer-line);padding-left:12px;position:relative}
.foot-col li::before{content:"";position:absolute;left:0;top:13px;width:4px;height:4px;background:var(--green)}
.foot-col li.current{color:var(--green)}
.contact h5{font-size:11px;font-weight:500;color:#d3d6d9;margin:14px 0 6px}
.contact p{font-size:10px;line-height:17px;color:#7f848a}
.bottom-bar{left:0;top:2562px;width:1200px;height:73px}
.copyright{left:159px;top:32px;font-size:10px;color:#c7b7a9}
.legal{right:158px;top:32px;font-size:10px;color:#c7b7a9;display:flex;gap:36px}
</style>
</head>
<body>

<header class="site-header wood abs">
  <div class="brand abs">
    <span class="brand-mark"></span>
    <div class="brand-text">
      <span class="brand-name">Thistlewood Joinery</span>
      <span class="brand-tagline">Kansas City's Premier Custom Kitchen<br>Cabinet Design Company</span>
    </div>
  </div>
  <div class="social abs"><span></span><span></span></div>
  <div class="call-note abs">We'd love to help. Call us today:</div>
  <div class="call-number abs">816.555.0142</div>
</header>

<nav class="main-nav abs">
  <a class="active" style="left:169px">Home</a>
  <a style="left:227px">Portfolio</a>
  <a style="left:300px">Kitchen Cabinets</a>
  <a style="left:416px">Cabinet Hardware</a>
  <a style="left:539px">Customer Experience</a>
  <a style="left:680px">Professional</a>
  <a style="left:773px">Who We Are</a>
  <a style="left:863px">Getting Started</a>
  <a style="left:972px">Contact Us</a>
</nav>

<section class="hero abs" role="img" aria-label="Photo of a warm wood custom kitchen with island, bar stools and a glass-walled dining area"></section>
<div class="hero-card abs">
  <p class="hero-eyebrow">ESTABLISHED IN 1966</p>
  <h1 class="hero-title">Best in the Midwest</h1>
  <p class="hero-copy">Thistlewood Joinery has long stood as one of the Midwest's most renowned makers of custom cabinets and fixtures.</p>
</div>
<div class="slide-arrow green abs" style="left:0;top:374px"><svg width="10" height="14" viewBox="0 0 10 14"><path d="M8 1 2 7l6 6" fill="none" stroke="#fff" stroke-width="2"/></svg></div>
<div class="slide-arrow abs" style="right:0;top:370px"><svg width="10" height="14" viewBox="0 0 10 14"><path d="M2 1l6 6-6 6" fill="none" stroke="#fff" stroke-width="2"/></svg></div>

<section class="categories abs">
  <div class="tile featured" style="left:162px;top:66px;background:linear-gradient(135deg,#c9cfc9,#7d8a7a)" role="img" aria-label="Photo of white kitchen cabinets"><div class="shade"></div><h3>Kitchens</h3><span class="btn">VIEW MORE</span></div>
  <div class="tile" style="left:463px;top:66px;background:linear-gradient(135deg,#d8d4cb,#8b877d)" role="img" aria-label="Photo of a bathroom vanity with arched mirror"><div class="shade"></div><h3>Bathroom</h3><span class="btn">VIEW MORE</span></div>
  <div class="tile" style="left:764px;top:66px;background:linear-gradient(135deg,#6b4128,#2f1a10)" role="img" aria-label="Photo of a wood-panelled office with bookshelves"><div class="shade"></div><h3>Office</h3><span class="btn">VIEW MORE</span></div>
  <div class="tile" style="left:162px;top:376px;background:linear-gradient(135deg,#d9d6d0,#7a6e63)" role="img" aria-label="Photo of a walk-in closet with shelving"><div class="shade"></div><h3>Closet/<br>Dressing</h3><span class="btn">VIEW MORE</span></div>
  <div class="tile" style="left:463px;top:376px;background:linear-gradient(135deg,#a8a39a,#4f4b45)" role="img" aria-label="Photo of a workshop with storage and a ladder"><div class="shade"></div><h3>Workshop</h3><span class="btn">VIEW MORE</span></div>
  <div class="tile" style="left:764px;top:376px;background:linear-gradient(135deg,#7a3a22,#2a120a)" role="img" aria-label="Photo of an entertainment bar in dark cherry wood"><div class="shade"></div><h3>Entertainment</h3><span class="btn">VIEW MORE</span></div>
</section>

<section class="showcase wood abs">
  <p class="showcase-eyebrow abs">WE BUILD CUSTOM CABINETS FOR YOU.</p>
  <h2 class="showcase-title abs">You dream it, we'll build it.</h2>
  <div class="shot abs" style="left:0;width:364px;background:linear-gradient(135deg,#3b4452,#1d232c)" role="img" aria-label="Photo of a navy kitchen island"></div>
  <div class="shot center abs" style="left:388px;width:424px;background:linear-gradient(160deg,#e8e6e2,#a9a49c 60%,#6d6760)" role="img" aria-label="Photo of a white kitchen with hood and granite island"></div>
  <div class="shot abs" style="left:836px;width:364px;background:linear-gradient(135deg,#d2d0cb,#5b5650)" role="img" aria-label="Photo of white cabinets with built-in oven"></div>
  <div class="slide-arrow abs" style="left:0;top:270px"><svg width="10" height="14" viewBox="0 0 10 14"><path d="M8 1 2 7l6 6" fill="none" stroke="#fff" stroke-width="2"/></svg></div>
  <div class="slide-arrow abs" style="right:0;top:270px"><svg width="10" height="14" viewBox="0 0 10 14"><path d="M2 1l6 6-6 6" fill="none" stroke="#fff" stroke-width="2"/></svg></div>
</section>

<h2 class="about-title abs">About Thistlewood Joinery</h2>
<div class="about-mark abs"></div>
<p class="about-copy abs">At <b>Thistlewood Joinery</b>, we've been designing and manufacturing the Midwest's finest custom cabinets and fixtures since 1966. From single cabinets to room remodels to entire home installations, our expert artisans help turn the house you live in to the home you've always dreamed of.</p>
<div class="learn-more abs">LEARN MORE <svg width="6" height="9" viewBox="0 0 6 9"><path d="M1 1l3.5 3.5L1 8" fill="none" stroke="#2b2f33" stroke-width="1.4"/></svg></div>
<div class="video abs" role="img" aria-label="Video player showing a white custom kitchen">
  <span class="video-title abs">Place Title For Movie Here</span>
  <div class="video-bar abs">
    <svg class="abs" style="left:6px;top:3px" width="8" height="8" viewBox="0 0 8 8"><path d="M0 0l8 4-8 4z" fill="#fff"/></svg>
    <div class="video-progress abs"></div>
  </div>
</div>

<footer class="site-footer abs">
  <div class="foot-col abs" style="left:162px;top:72px">
    <h4>Navigation</h4>
    <ul><li>Home</li><li>Who We Are</li><li>Getting Started</li><li>Contact Us</li><li>Customer Experience</li><li>Professional</li><li>Cabinet Hardware</li></ul>
  </div>
  <div class="foot-col abs" style="left:387px;top:72px">
    <h4>Portfolio</h4>
    <ul><li>Kitchen Cabinets</li><li class="current">Kitchen Islands</li><li>Bathroom Cabinets</li><li>Bookcase</li><li>Closets</li><li>Entertainment Centers</li><li>TV Cabinets</li></ul>
  </div>
  <div class="foot-col abs" style="left:611px;top:102px">
    <ul><li>Garage</li><li>Commercial</li><li>Wood hood</li><li>Hutch</li><li>Custom Built Bars</li><li>Door &amp; Drawer Styles</li></ul>
  </div>
  <div class="foot-col contact abs" style="left:836px;top:72px">
    <h4>Contact Information</h4>
    <h5>Store</h5>
    <p>4820 Harlow Street<br>Millbrook, MO 64000</p>
    <h5>Phone Number</h5>
    <p>Phone: 816.555.0142<br>Fax: 816.555.0187</p>
    <h5>Email Address</h5>
    <p>info@thistlewoodjoinery.example</p>
  </div>
</footer>

<div class="bottom-bar wood abs">
  <p class="copyright abs">Copyright 2015 Thistlewood Joinery &nbsp;|&nbsp; All Rights Reserved</p>
  <div class="legal abs"><span>Privacy Policy</span><span>Sitemap</span></div>
</div>

</body>
</html>
```